Maralby Information Posters for Student signage

Secondary school looking for some posters to display throughout the school with fresh designs using school colours and fitting with general feel of the school's graphic image. The final designs should be welcoming but clearly outline the required instructions. Sample designs that have been created by the school are attached with the relevant information that is required to appear on the signs. School would like a more dynamic design than the basic signs attached.
We are looking for:
- Large pop-up banner style size for the 2 posters called
"Ready for class" and "Morning Routine".
- Printable poster for the "Maralby Outdoor" sign.

Please incorporate a design feature of "the Maralby 1,2,3" into the posters and also use the Maralby Leaner values of Integrity, Compassion, Curiosity and Drive to help illustrate the content.

An option for design is to incorporate our school's first nations artwork into the design and i have also provided various extracts of design pieces that the school often uses in it's marketing materials.

Target Market(s)

Secondary School Students

Industry/Entity Type

Education

Colors
00AB8E
00BBA5
67D7C9
C6EFE9
E9F9F6
FFF300
FFF600
FEFA6F
FFFEC7
FFFEE8
FFC000
F8CF3A
FAE287
FDF2CF
FEFAEE

Requirements
Must have
• My project must have eyecatching graphics

```html
<!DOCTYPE html>
<html lang="en">
<head>
<meta charset="utf-8">
<title>Maralby Information Posters</title>
<link rel="stylesheet" href="https://fonts.googleapis.com/css2?family=Teko:wght@500;600&family=Archivo:ital,wght@0,600;0,800;0,900;1,800&display=swap">
<style>
:root{
  --green-deep:#06391a;
  --green:#0b5a25;
  --green-bright:#1b8a34;
  --yellow:#ffec00;
  --yellow-soft:#fff600;
  --white:#ffffff;
  --paper:#f4f5f1;
  --ink:#0a3d1c;
  --bg:#e4e5e3;
}
*{box-sizing:border-box;margin:0;padding:0}
html,body{width:1200px;height:1068px;overflow:hidden;background:var(--bg);font-family:"Archivo",Arial,sans-serif}
.canvas{position:relative;width:1200px;height:1068px}

.poster{position:absolute;overflow:hidden;box-shadow:0 6px 18px rgba(0,0,0,.28);background:var(--white)}
.poster--portrait{width:380px;height:540px;top:30px}
.poster--hats{left:150px}
.poster--class{left:670px}
.poster-shapes{position:absolute;inset:0}

.headline{position:absolute;left:20px;top:18px;font-family:"Teko",Impact,sans-serif;font-weight:600;font-size:32px;line-height:25px;color:var(--white);text-transform:uppercase;letter-spacing:.3px}
.headline .hl{color:var(--yellow)}
.headline--large{font-size:42px;line-height:34px}

.brand-123{position:absolute;left:186px;top:22px;width:172px;height:76px;background:var(--yellow);border-radius:8px;padding:6px}
.brand-123__name{background:var(--white);border-radius:5px;height:30px;text-align:center;font-weight:900;font-size:19px;line-height:30px;color:var(--ink)}
.brand-123__steps{display:flex;justify-content:space-around;margin-top:6px}
.step-dot{width:26px;height:26px;border-radius:50%;background:var(--ink);color:var(--white);font-weight:800;font-size:13px;line-height:26px;text-align:center;border:2px solid var(--white)}

.rule-list{position:absolute;left:176px;top:118px;list-style:none}
.rule{display:flex;align-items:center;height:106px}
.icon{width:84px;height:84px;border-radius:50%;border:4px dotted var(--yellow);padding:4px;background:var(--ink);background-clip:content-box;display:flex;align-items:center;justify-content:center;flex:none}
.icon svg{width:42px;height:42px}
.rule__text{margin-left:14px;color:var(--ink);font-weight:800;font-size:17px;line-height:18px}
.rule__num{display:block;width:34px;height:34px;border-radius:50%;background:var(--yellow);text-align:center;font-size:26px;line-height:34px;font-weight:900;margin-bottom:4px}
.rule__note{display:block;font-weight:600;font-size:13px}

.values{position:absolute;left:20px;color:var(--white)}
.values__name{font-weight:800;font-size:15px;line-height:17px}
.values__tag{color:var(--yellow);font-weight:600;font-size:11px;line-height:14px;margin-top:4px}

.school-mark{position:absolute;display:flex;align-items:center;gap:6px;font-weight:900;font-size:17px;color:var(--ink)}
.school-mark__dot{width:14px;height:14px;border-radius:50%;background:var(--ink)}

.poster--routine{left:300px;top:610px;width:600px;height:422px;background:var(--green)}
.routine-title{position:absolute;left:205px;top:12px;font-family:"Teko",Impact,sans-serif;font-weight:600;font-size:60px;line-height:60px;color:var(--white)}
.routine-sub{position:absolute;left:205px;top:76px;display:flex;align-items:center;gap:8px;color:var(--yellow);font-style:italic;font-weight:800;font-size:15px}
.routine-sub::before{content:"";width:80px;height:2px;background:var(--white)}
.tab{position:absolute;top:112px;height:28px;background:var(--white);transform:skewX(-10deg);text-align:center;font-style:italic;font-weight:800;font-size:17px;line-height:28px;color:var(--ink)}
.tab--on{left:180px;width:160px}
.tab--late{left:392px;width:160px}
.divider{position:absolute;left:366px;top:112px;width:2px;height:258px;background:rgba(255,255,255,.7)}
.routine-list{position:absolute;top:158px;list-style:none}
.routine-list--on{left:172px}
.routine-list--late{left:384px}
.routine-step{display:flex;align-items:flex-start;height:74px}
.routine-step .icon{width:64px;height:64px;border:3px dotted var(--yellow);padding:3px;background:var(--white);background-clip:content-box}
.routine-step .icon svg{width:32px;height:32px}
.routine-step__text{margin-left:8px;color:var(--white);font-weight:800;font-size:10.5px;line-height:12px}
.routine-step__num{display:block;width:24px;height:24px;border-radius:50%;background:var(--yellow);color:var(--ink);text-align:center;font-size:17px;line-height:24px;font-weight:900;margin-bottom:3px}
.brand-123--routine{left:22px;top:22px;width:160px;height:74px}
.brand-123--routine .brand-123__name{font-size:18px}
</style>
</head>
<body>
<main class="canvas">

  <!-- Outdoor hats poster -->
  <section class="poster poster--portrait poster--hats" aria-label="Maralby Outdoor poster">
    <svg class="poster-shapes" viewBox="0 0 380 540" aria-hidden="true">
      <defs>
        <linearGradient id="gDeep" x1="0" y1="0" x2="1" y2="1"><stop offset="0" stop-color="#0b5a25"/><stop offset="1" stop-color="#06391a"/></linearGradient>
        <linearGradient id="gBand" x1="0" y1="0" x2="1" y2="0"><stop offset="0" stop-color="#0b5a25"/><stop offset=".7" stop-color="#1b8a34"/><stop offset="1" stop-color="#d8e400"/></linearGradient>
      </defs>
      <rect width="380" height="540" fill="#f4f5f1"/>
      <polygon points="0,0 178,0 136,540 0,540" fill="url(#gDeep)"/>
      <polygon points="150,510 380,452 380,540 140,540" fill="url(#gBand)"/>
      <polygon points="0,444 238,416 262,540 0,540" fill="#ffec00"/>
    </svg>
    <h2 class="headline">We wear<br><span class="hl">hats at<br>Maralby</span><br>when<br>outdoors...</h2>
    <div class="brand-123"><div class="brand-123__name">The Maralby</div><div class="brand-123__steps"><span class="step-dot">1</span><span class="step-dot">2</span><span class="step-dot">3</span></div></div>
    <ul class="rule-list">
      <li class="rule"><div class="icon" role="img" aria-label="Walking figure pictogram"></div><p class="rule__text"><span class="rule__num">1</span>Walking</p></li>
      <li class="rule"><div class="icon" role="img" aria-label="Seated figure pictogram"></div><p class="rule__text"><span class="rule__num">2</span>Sitting</p></li>
      <li class="rule"><div class="icon" role="img" aria-label="Figure kicking a ball pictogram"></div><p class="rule__text"><span class="rule__num">3</span>Playing</p></li>
    </ul>
    <div class="values" style="top:352px"><p class="values__name">Integrity</p><p class="values__tag">Maralby Learner<br>Values.</p></div>
    <div class="school-mark" style="left:26px;top:476px"><span class="school-mark__dot"></span>Maralby</div>
  </section>

  <!-- Ready for class poster -->
  <section class="poster poster--portrait poster--class" aria-label="Ready for class poster">
    <svg class="poster-shapes" viewBox="0 0 380 540" aria-hidden="true">
      <rect width="380" height="540" fill="#f4f5f1"/>
      <polygon points="0,0 178,0 136,540 0,540" fill="url(#gDeep)"/>
      <polygon points="150,510 380,452 380,540 140,540" fill="url(#gBand)"/>
      <polygon points="0,444 238,416 262,540 0,540" fill="#ffec00"/>
    </svg>
    <h2 class="headline headline--large">Are you<br><span class="hl">ready</span><br>for<br><span class="hl">class?</span></h2>
    <div class="brand-123"><div class="brand-123__name">The Maralby</div><div class="brand-123__steps"><span class="step-dot">1</span><span class="step-dot">2</span><span class="step-dot">3</span></div></div>
    <ul class="rule-list">
      <li class="rule"><div class="icon"><svg viewBox="0 0 40 40" aria-hidden="true"><rect x="8" y="9" width="24" height="16" rx="2" fill="none" stroke="#fff" stroke-width="3"/><path d="M4 29h32l-2 4H6z" fill="#fff"/></svg></div><p class="rule__text"><span class="rule__num">1</span>Laptop /<br>Workbook</p></li>
      <li class="rule"><div class="icon"><svg viewBox="0 0 40 40" aria-hidden="true"><rect x="11" y="4" width="18" height="32" rx="5" fill="#fff"/><circle cx="20" cy="10" r="2.5" fill="#0a3d1c"/><rect x="14" y="16" width="12" height="16" rx="2" fill="#0a3d1c"/></svg></div><p class="rule__text"><span class="rule__num">2</span>Phone in<br>Pouchlok</p></li>
      <li class="rule"><div class="icon"><svg viewBox="0 0 40 40" aria-hidden="true"><path d="M14 4l6 4 6-4 10 6-4 7-4-2v9H12v-9l-4 2-4-7z" fill="#fff"/><path d="M12 26h16l-1 11h-5l-2-7-2 7h-5z" fill="#fff"/></svg></div><p class="rule__text"><span class="rule__num">3</span>Correct<br>Uniform<span class="rule__note">(Including hat)</span></p></li>
    </ul>
    <div class="values" style="top:340px"><p class="values__name">Curiosity<br>and Drive</p><p class="values__tag">Maralby Learner<br>Values.</p></div>
    <div class="school-mark" style="left:26px;top:476px"><span class="school-mark__dot"></span>Maralby</div>
  </section>

  <!-- Morning routine poster -->
  <section class="poster poster--routine" aria-label="Morning routine poster">
    <svg class="poster-shapes" viewBox="0 0 600 422" aria-hidden="true">
      <defs>
        <linearGradient id="gRoutine" x1="0" y1="0" x2="1" y2="1"><stop offset="0" stop-color="#1b8a34"/><stop offset=".5" stop-color="#0b5a25"/><stop offset="1" stop-color="#06391a"/></linearGradient>
        <linearGradient id="gCorner" x1="0" y1="0" x2="1" y2="0"><stop offset="0" stop-color="#06391a" stop-opacity="0"/><stop offset="1" stop-color="#d8e400"/></linearGradient>
      </defs>
      <rect width="600" height="422" fill="url(#gRoutine)"/>
      <rect x="420" y="360" width="180" height="62" fill="url(#gCorner)"/>
      <polygon points="0,300 130,288 144,422 0,422" fill="#ffec00"/>
    </svg>
    <div class="brand-123 brand-123--routine"><div class="brand-123__name">The Maralby</div><div class="brand-123__steps"><span class="step-dot">1</span><span class="step-dot">2</span><span class="step-dot">3</span></div></div>
    <h2 class="routine-title">MORNING ROUTINE</h2>
    <p class="routine-sub">Early is on time, on time is late!</p>
    <div class="tab tab--on">ON TIME</div>
    <div class="tab tab--late">RUNNIG LATE</div>
    <div class="divider"></div>
    <ul class="routine-list routine-list--on">
      <li class="routine-step"><div class="icon"><svg viewBox="0 0 40 40" aria-hidden="true"><circle cx="20" cy="20" r="14" fill="none" stroke="#0a3d1c" stroke-width="3.5"/><path d="M20 11v10l6 4" fill="none" stroke="#0a3d1c" stroke-width="3"/></svg></div><p class="routine-step__text"><span class="routine-step__num">1</span>Arrive before<br>8:30 AM</p></li>
      <li class="routine-step"><div class="icon"><svg viewBox="0 0 40 40" aria-hidden="true"><rect x="5" y="6" width="9" height="28" fill="#0a3d1c"/><rect x="16" y="6" width="9" height="28" fill="#0a3d1c"/><rect x="27" y="6" width="9" height="28" fill="#0a3d1c"/></svg></div><p class="routine-step__text"><span class="routine-step__num">2</span>Place Bag<br>in Locker</p></li>
      <li class="routine-step"><div class="icon" role="img" aria-label="Group at desk pictogram"></div><p class="routine-step__text"><span class="routine-step__num">3</span>Arrive at<br>Home Group /<br>House Assembly<br>before 8:40 AM</p></li>
    </ul>
    <ul class="routine-list routine-list--late">
      <li class="routine-step"><div class="icon"><svg viewBox="0 0 40 40" aria-hidden="true"><path d="M20 5l15 9H5z" fill="#0a3d1c"/><rect x="7" y="15" width="26" height="19" fill="#0a3d1c"/><rect x="17" y="24" width="6" height="10" fill="#fff"/></svg></div><p class="routine-step__text"><span class="routine-step__num">1</span>Sign in at<br>Student Services</p></li>
      <li class="routine-step"><div class="icon"><svg viewBox="0 0 40 40" aria-hidden="true"><rect x="5" y="6" width="9" height="28" fill="#0a3d1c"/><rect x="16" y="6" width="9" height="28" fill="#0a3d1c"/><rect x="27" y="6" width="9" height="28" fill="#0a3d1c"/></svg></div><p class="routine-step__text"><span class="routine-step__num">2</span>Place bag<br>n Locker</p></li>
      <li class="routine-step"><div class="icon" role="img" aria-label="Group at desk pictogram"></div><p class="routine-step__text"><span class="routine-step__num">3</span>Prompt arrival<br>to class expected</p></li>
    </ul>
    <div class="values" style="top:214px;left:22px"><p class="values__name" style="font-size:18px">Integrity</p><p class="values__tag" style="font-size:13px;line-height:16px">Maralby Learner<br>Values.</p></div>
    <div class="school-mark" style="left:24px;top:350px"><span class="school-mark__dot"></span>Maralby</div>
  </section>

</main>
</body>
</html>
```